Bright Horizon Painting and Remodeling needs a business card

Business card should have company logo. I will upload two different logos and let me see which one is a better design for the business card.

Name of company: Bright Horizon Painting and Remodeling
Address: 4126 NW 71st st Suite 214
Miami, FL 33166

local phone: (305) 555-0142
toll free (855) 555-0197
fax (866) 555-0163

email: corinne@paintingbrighthorizon.example

not sure if i should include social media links or names on the business card.

company does interior and exterior painting, pressure washing, wall paper removal, drywall and stucco repair, staining,

We give free estimates.

I want a two sided business card.

Not sure if all this information is necessary for the business card. Designer can pick out whatever information they deem is important for a consumer to see on the business card.

Anticipating on the business card to be printed on nice quality.

I will upload an image of one of the logos on a type of business card surface. That idea can be used as well. Be creative. Business card should be professional but very nice and eye catching.

remove drywall and stucco repair and replace with tile installation

Industry/Entity Type

Business

Contact Information for Business Card

Miami, FL 33166

toll free (855) 555-0197
fax (866) 555-0163

company does interior and exterior painting, pressure washing, wall paper removal, drywall and stucco repair, staining, tile removal, *specializing in vinyl floor removal

free estimates.

Requirements
Must have
• Profesional font

```html
<!DOCTYPE html>
<html lang="en">
<head>
<meta charset="utf-8">
<title>Bright Horizon Painting and Remodeling — Business Card</title>
<link href="https://fonts.googleapis.com/css2?family=Tinos:wght@400;700&family=Open+Sans:wght@400&display=swap" rel="stylesheet">
<style>
  :root {
    --page: #e6e6e6;
    --purple: #9b6fc9;
    --purple-icon: #9466c4;
    --charcoal: #332e2f;
    --white: #ffffff;
    --ink: #333030;
    --shadow: rgba(0,0,0,0.22);
  }
  * { margin: 0; padding: 0; box-sizing: border-box; }
  html, body {
    width: 1200px; height: 987px; overflow: hidden;
    background: var(--page);
  }
  .canvas { position: relative; width: 1200px; height: 987px; }
  .card {
    position: absolute; left: 293px; width: 615px; height: 351px;
    overflow: hidden; box-shadow: 0 2px 4px var(--shadow);
  }
  .card--front { top: 130px; background: var(--purple); }
  .card--back  { top: 505px; background: var(--charcoal); }

  .front-shape { position: absolute; inset: 0; }

  .contact {
    position: absolute; left: 35px; top: 36px;
    color: var(--white); font-family: "Tinos", "Times New Roman", serif;
  }
  .contact__name { font-size: 23px; font-weight: 700; letter-spacing: 0.5px; }
  .contact__title { font-size: 17px; margin-top: 2px; }
  .contact__address { font-size: 17px; line-height: 22.5px; margin-top: 32px; }
  .contact__list { list-style: none; margin-top: 14px; font-size: 16px; }
  .contact__list li { display: flex; align-items: center; height: 23.5px; white-space: nowrap; }
  .contact__list .contact__email { font-size: 13.5px; }
  .contact__list .contact__web { font-size: 14.5px; }
  .contact__list svg { width: 15px; height: 15px; margin-right: 8px; flex: none; fill: var(--white); }

  .brand {
    position: absolute; text-align: center;
    font-family: "Tinos", "Times New Roman", serif; font-weight: 700;
    text-transform: uppercase; letter-spacing: 1.5px;
  }
  .brand--front {
    left: 300px; top: 92px; width: 300px;
    color: var(--ink); font-size: 25px; line-height: 30px;
  }
  .brand--front .brand__sub { font-size: 14px; line-height: 20px; letter-spacing: 3px; }
  .brand--back {
    left: 0; right: 0; top: 140px;
    color: var(--white); font-size: 33px; line-height: 40px;
  }
  .brand--back .brand__sub { font-size: 16px; line-height: 24px; letter-spacing: 4px; }
  .brand__mark {
    display: block; margin: 0 auto 10px; border-radius: 50%;
    background: var(--purple);
  }
  .brand--front .brand__mark { width: 34px; height: 34px; }

  .social {
    position: absolute; right: 17px; top: 11px; display: flex; gap: 2px; list-style: none;
  }
  .social li { width: 21px; height: 21px; border-radius: 50%; background: var(--purple-icon); }

  .website {
    position: absolute; left: 0; right: 0; top: 306px; text-align: center;
    color: var(--white); font-family: "Open Sans", Arial, sans-serif;
    font-size: 16px; letter-spacing: 4.5px;
  }
</style>
</head>
<body>
<main class="canvas">
  <section class="card card--front" aria-label="Business card front">
    <svg class="front-shape" viewBox="0 0 615 351" aria-hidden="true">
      <path d="M422 0 C300 20 225 90 234 150 C240 230 300 300 380 325 C450 345 540 351 615 351 L615 0 Z" fill="var(--charcoal)"/>
      <path d="M442 0 C330 25 258 95 258 155 C262 225 322 290 402 318 C470 340 545 348 615 348 L615 0 Z" fill="var(--white)"/>
    </svg>

    <div class="contact">
      <p class="contact__name">DANIEL REYES</p>
      <p class="contact__title">CEO/Founder</p>
      <p class="contact__address">4126 NW 71st st<br>Suite 214<br>Miami, FL 33166</p>
      <ul class="contact__list">
        <li><svg viewBox="0 0 16 16"><path d="M3.5 1.5l2.3 0 1 3.4-1.6 1.3c.9 1.9 2.3 3.3 4.2 4.2l1.3-1.6 3.4 1v2.3c0 .9-.8 1.6-1.7 1.5C6.6 13.1 2.9 9.4 2 3.2 1.9 2.3 2.6 1.5 3.5 1.5z"/></svg>(305) 555-0142</li>
        <li><svg viewBox="0 0 16 16"><path d="M4.5 0.5h7a1 1 0 0 1 1 1v13a1 1 0 0 1-1 1h-7a1 1 0 0 1-1-1v-13a1 1 0 0 1 1-1zm.6 2v9.5h5.8V2.5zM8 12.8a.9.9 0 1 0 0 1.8.9.9 0 0 0 0-1.8z"/></svg>(855) 555-0197 (T)</li>
        <li><svg viewBox="0 0 16 16"><path d="M4 1h8v4H4zM1 6h14v6h-2.5v-2h-9v2H1zM4.5 11h7v4h-7z"/></svg>(866) 555-0163</li>
        <li class="contact__email"><svg viewBox="0 0 16 16"><path d="M1 3.5h14v9H1zm1.2 1 5.8 4.3 5.8-4.3z"/></svg>corinne@paintingbrighthorizon.example</li>
        <li class="contact__web"><svg viewBox="0 0 16 16"><path d="M8 1a7 7 0 1 0 0 14A7 7 0 0 0 8 1zm-1 1.8c-.3 1 .5 1.4 1.2 1.8.8.5.4 1.6-.5 1.7-1.3.2-2.4.4-2.2 1.9.2 1.3 1.6 1.2 1.8 2.4.1.8-.3 1.7-.5 2.4A5.6 5.6 0 0 1 7 2.8zm3.2 10.9c.3-1 .9-1.8 1.7-2.6.6-.6.2-1.6-.6-1.7-1-.1-1.3-.9-.7-1.6.5-.6 1.6-.5 2-.1a5.6 5.6 0 0 1-2.4 6z"/></svg>www.paintingbrighthorizon.example</li>
      </ul>
    </div>

    <div class="brand brand--front">
      <span class="brand__mark" aria-hidden="true"></span>
      <p>Bright Horizon</p>
      <p class="brand__sub">Painting and Remodeling</p>
    </div>
  </section>

  <section class="card card--back" aria-label="Business card back">
    <ul class="social" aria-label="Social media">
      <li></li><li></li><li></li><li></li>
    </ul>
    <div class="brand brand--back">
      <p>Bright Horizon</p>
      <p class="brand__sub">Painting and Remodeling</p>
    </div>
    <p class="website">www.paintingbrighthorizon.example</p>
  </section>
</main>
</body>
</html>
```